Business Development website and logo (www.kwalrun.eu)

Based on an existing website structure (http://tamford.velunquo.com) fully redesign the site including: colors, images, technology and logo. Kwalrun is intended to provide Europe and LATAM Business Development services. The site and logo should communicate modern, professional and experienced sales services.

Target Market(s)

Tech companies wanting to expand into new territories

Industry/Entity Type

Tech

Logo Text

It has to be an abstract design, no letters

Coding

Coded - Design and coding required

Number of Pages Required

5+ page

Font styles to use
Sans Serif

Colors

Designer to choose colors to be used in the design.

Requirements
Must have
• - The site and logo should communicate modern, professional and experienced sales services.
• - All the pages included in the example site: http://tamford.velunquo.com (Company, Careers, Bs Dev, Sales, etc..)
Nice to have
• - Sober design
Should not have
• - Fun design as this one: http://velunquo.com/

```html
<!DOCTYPE html>
<html lang="en">
<head>
<meta charset="utf-8">
<title>Tamford — Business &amp; Operations Enabler</title>
<link href="https://fonts.googleapis.com/css2?family=Rubik:wght@400;500;700&family=Roboto:wght@400;500&display=swap" rel="stylesheet">
<style>
:root{
  --ink:#1f2433;
  --body:#3a3f4c;
  --muted:#5c6170;
  --orange:#fb9c10;
  --blue:#1a4fb5;
  --navy:#0e2b4f;
  --lavender:#f4f3f8;
  --wave:#e6e4f1;
  --sand:#f6f2f2;
  --white:#ffffff;
  --rule:#c9cbd3;
  --art-light:#e3e8f4;
  --art-mid:#aebde6;
  --art-deep:#3552b0;
}
*{margin:0;padding:0;box-sizing:border-box}
html,body{width:1200px;height:4199px;overflow:hidden}
body{position:relative;background:var(--white);font-family:'Roboto',sans-serif;color:var(--body)}
.abs{position:absolute}
h1,h2,h3,h4,.nav a,.btn,.brand{font-family:'Rubik',sans-serif}
.btn{position:absolute;display:flex;align-items:center;justify-content:center;background:var(--orange);color:var(--white);font-size:13px;font-weight:500;letter-spacing:.4px;border-radius:3px;text-decoration:none;height:31px}
.brand{position:absolute;display:flex;flex-direction:column;align-items:center;color:#2b3040;font-weight:400}
.brand .mark{width:50px;height:50px;border-radius:50%;background:var(--blue)}
.brand span{font-size:17px;margin-top:8px}

/* header + hero */
.hero-bg{left:0;top:0;width:1200px;height:640px}
.nav{position:absolute;top:34px;left:0;width:1200px;height:20px}
.nav a{position:absolute;font-size:14px;color:var(--ink);text-decoration:none;font-weight:500}
.nav a.active{color:var(--orange);border-bottom:1px solid var(--orange)}
.hero-title{left:130px;top:218px;font-size:34px;line-height:41px;font-weight:700;color:var(--ink);letter-spacing:.3px}
.hero-sub{left:130px;top:313px;font-size:20px;color:var(--ink);font-family:'Roboto',sans-serif}
.hero-art{left:560px;top:110px;width:500px;height:450px;border-radius:46% 54% 30% 40% / 50% 45% 25% 35%;background:linear-gradient(160deg,#e1e7f5 0%,#c7d2ef 45%,#5b74c9 75%,#f7941d 100%)}

/* section headings */
.section-title{position:absolute;left:0;width:1200px;text-align:center;font-size:24px;font-weight:500;color:var(--ink);letter-spacing:.3px}
.underline{position:absolute;left:572px;width:56px;height:3px;background:var(--blue)}

.welcome-text{left:357px;top:745px;width:486px;text-align:center;font-size:15px;line-height:21px;color:var(--body)}

/* services */
.services{left:0;top:962px;width:1200px;height:1827px;background:var(--sand)}
.service .dash{position:absolute;width:28px;height:2px;background:#9aa0ab}
.service h3{position:absolute;font-size:18px;font-weight:500;color:var(--ink);letter-spacing:.2px}
.service p{position:absolute;width:338px;font-size:14.5px;line-height:21px;color:var(--body)}
.service-art{position:absolute;border-radius:52% 48% 44% 56% / 50% 46% 54% 50%;background:linear-gradient(150deg,var(--art-light) 0%,var(--art-mid) 55%,var(--art-deep) 100%)}

/* risk free band */
.risk{left:0;top:2789px;width:1200px;height:500px;background:var(--navy)}
.risk-art{left:238px;top:2895px;width:318px;height:300px;border-radius:6px;background:linear-gradient(160deg,#c9bdf5 0%,#8f7fdc 55%,#f28a78 100%)}
.risk h2{position:absolute;left:722px;top:2891px;font-size:24px;font-weight:500;color:var(--white);letter-spacing:.5px}
.risk .bar{position:absolute;left:725px;top:2929px;width:54px;height:3px;background:var(--blue)}
.risk p{position:absolute;left:725px;top:2960px;width:362px;font-size:14.5px;line-height:21px;color:#e6ebf3}

/* blog */
.card{position:absolute;top:3430px;width:299px;height:345px;border:1px solid var(--rule);background:var(--white)}
.card .photo{position:absolute;left:15px;top:14px;width:269px;height:158px}
.card .date{position:absolute;left:15px;top:161px;background:var(--white);font-size:11px;color:var(--muted);padding:3px 8px 2px 22px}
.card h4{position:absolute;left:25px;top:197px;font-size:13px;font-weight:500;color:var(--ink)}
.card p{position:absolute;left:25px;top:220px;width:250px;font-size:12px;line-height:15.5px;color:var(--body)}
.card .btn{left:31px;top:290px;width:95px;height:30px}

/* footer */
.footer-bg{left:0;top:3805px;width:1200px;height:394px}
.foot-col{position:absolute;top:3974px}
.foot-col h4{font-size:14px;font-weight:500;color:var(--ink);margin-bottom:12px}
.foot-col li{list-style:none;font-size:12.5px;line-height:19.5px;color:#474c59}
.foot-rule{left:130px;top:4116px;width:941px;height:1px;background:#c4c6cf}
.copyright{left:0;top:4152px;width:1200px;text-align:center;font-size:12px;color:#3f4452}
</style>
</head>
<body>

<svg class="abs hero-bg" viewBox="0 0 1200 640" aria-hidden="true">
  <path d="M0 0H1200V545C1080 640 900 640 700 600C480 560 320 520 170 540C90 550 30 575 0 595Z" fill="var(--lavender)"/>
  <path d="M0 595C30 575 90 550 170 540C320 520 480 560 700 600C900 640 1080 640 1200 545V570C1080 650 900 650 700 612C480 572 320 535 170 552C90 562 30 585 0 605Z" fill="var(--wave)"/>
</svg>

<header>
  <div class="brand" style="left:128px;top:20px">
    <div class="mark"></div>
    <span>tamford</span>
  </div>
  <nav class="nav">
    <a class="active" style="left:559px" href="#">HOME</a>
    <a style="left:629px" href="#">WHO WE ARE</a>
    <a style="left:751px" href="#">BSNS DEV &amp; SALES</a>
    <a style="left:911px" href="#">SERVICES</a>
    <a style="left:1006px" href="#">CONTACT</a>
  </nav>
</header>

<section class="hero">
  <h1 class="abs hero-title">YOUR KEY TO THE LATIN<br>AMERICAN MARKET</h1>
  <p class="abs hero-sub">Business &amp; Operations Enabler</p>
  <a class="btn" style="left:130px;top:368px;width:116px;height:33px" href="#">READ MORE</a>
  <div class="abs hero-art" role="img" aria-label="Illustration of a businessman with a briefcase running up a rising orange growth arrow, with plants, gears and clouds"></div>
</section>

<section class="welcome">
  <h2 class="section-title" style="top:668px">WELCOME TO OUR SITE</h2>
  <div class="underline" style="top:710px"></div>
  <p class="abs welcome-text">Founded in 2005, Tamford has implemented a vast amount of<br>telecom projects worldwide, including Prepaid, IN and SMS platforms.<br>Our Clients are technology providers wanting to enter the American<br>Continent and they find in Tamford an experienced team to introduce<br>their brand without too many financial and human risks.</p>
  <a class="btn" style="left:553px;top:878px;width:104px" href="#">READ MORE</a>
</section>

<div class="abs services"></div>
<section>
  <h2 class="section-title" style="top:1011px">OUR SERVICES</h2>
  <div class="underline" style="top:1054px"></div>

  <article class="service">
    <div class="service-art" style="left:184px;top:1120px;width:422px;height:380px" role="img" aria-label="Isometric illustration of a team working around a meeting table with laptops"></div>
    <div class="dash" style="left:691px;top:1158px"></div>
    <h3 style="left:691px;top:1169px">BUSINESS DEVELOPMENT</h3>
    <p style="left:694px;top:1211px">There are many variations of passages of Lorem Ipsum available, but the majority have suffered alteration in some form, by injected humour, or randomised words which don't look even slightly believable. If you are going to use a passage of Lorem Ipsum, you need to be sure there.</p>
    <a class="btn" style="left:694px;top:1368px;width:106px" href="#">READ MORE</a>
  </article>

  <article class="service">
    <div class="dash" style="left:188px;top:1584px"></div>
    <h3 style="left:188px;top:1596px">PROJECT DEPLOYMENT</h3>
    <p style="left:190px;top:1640px">There are many variations of passages of Lorem Ipsum available, but the majority have suffered alteration in some form, by injected humour, or randomised words which don't look even slightly believable. If you are going to use a passage of Lorem Ipsum, you need to be sure there.</p>
    <a class="btn" style="left:192px;top:1796px;width:105px" href="#">READ MORE</a>
    <div class="service-art" style="left:611px;top:1500px;width:416px;height:385px" role="img" aria-label="Isometric illustration of a rocket launching from a laptop with people and dashboards"></div>
  </article>

  <article class="service">
    <div class="service-art" style="left:196px;top:1945px;width:391px;height:385px" role="img" aria-label="Isometric illustration of large gears, a magnifier and charts with two people"></div>
    <div class="dash" style="left:691px;top:1990px"></div>
    <h3 style="left:691px;top:1999px">QUALITY PROCESS</h3>
    <p style="left:694px;top:2042px">There are many variations of passages of Lorem Ipsum available, but the majority have suffered alteration in some form, by injected humour, or randomised words which don't look even slightly believable. If you are going to use a passage of Lorem Ipsum, you need to be sure there.</p>
    <a class="btn" style="left:694px;top:2198px;width:106px" href="#">READ MORE</a>
  </article>

  <article class="service">
    <div class="dash" style="left:188px;top:2424px"></div>
    <h3 style="left:188px;top:2435px">CUSTOMER SUPPORT</h3>
    <p style="left:190px;top:2479px">There are many variations of passages of Lorem Ipsum available, but the majority have suffered alteration in some form, by injected humour, or randomised words which don't look even slightly believable. If you are going to use a passage of Lorem Ipsum, you need to be sure there.</p>
    <a class="btn" style="left:192px;top:2635px;width:105px" href="#">READ MORE</a>
    <div class="service-art" style="left:628px;top:2345px;width:402px;height:390px" role="img" aria-label="Isometric illustration of a support agent with headset on a laptop screen, chat bubbles and a lightbulb"></div>
  </article>
</section>

<section>
  <div class="abs risk"></div>
  <div class="abs risk-art" role="img" aria-label="Illustration of a team building a web page layout together, with plants and a ladder"></div>
  <div class="risk">
    <h2>RISK FREE INSTANT ACCESS</h2>
    <div class="bar"></div>
    <p>Lorem ipsum dolor sit amet, consectetur adipiscing elit, sed do eiusmod tempor incididunt ut labore et dolore magna aliqua. Ut enim ad minim veniam, quis nostrud exercitation ullamco laboris nisi ut aliquip ex ea commodo consequat. Duis aute irure dolor in reprehenderit in voluptate velit esse cillum dolore eu fugiat nulla pariatur. Excepteur sint occaecat cupidatat non proident.</p>
    <a class="btn" style="left:727px;top:3161px;width:106px" href="#">READ MORE</a>
  </div>
</section>

<section>
  <h2 class="section-title" style="top:3341px">LATEST BLOG</h2>
  <div class="underline" style="top:3383px"></div>

  <article class="card" style="left:130px">
    <div class="photo" role="img" aria-label="Photo of hands reviewing printed financial charts with a pen" style="background:linear-gradient(135deg,#d8dbe2,#9aa3b4 60%,#6f84b8)"></div>
    <span class="date">28 Dec,2019</span>
    <h4>SED UT PERSPICIATIS UNDE</h4>
    <p>There are many variations of passages of Lorem Ipsum available, but the majority have suffered alteration in some</p>
    <a class="btn" href="#">READ MORE</a>
  </article>

  <article class="card" style="left:452px">
    <div class="photo" role="img" aria-label="Photo of a team planning over papers and a laptop on a desk" style="background:linear-gradient(135deg,#b49c88,#8c7f78 50%,#d9cfc6)"></div>
    <span class="date">28 Dec,2019</span>
    <h4>SED UT PERSPICIATIS UNDE</h4>
    <p>There are many variations of passages of Lorem Ipsum available, but the majority have suffered alteration in some</p>
    <a class="btn" href="#">READ MORE</a>
  </article>

  <article class="card" style="left:773px">
    <div class="photo" role="img" aria-label="Overhead photo of a business meeting around a table" style="background:linear-gradient(135deg,#e3e3e3,#a8a6a4 55%,#6e6a66)"></div>
    <span class="date">28 Dec,2019</span>
    <h4>SED UT PERSPICIATIS UNDE</h4>
    <p>There are many variations of passages of Lorem Ipsum available, but the majority have suffered alteration in some</p>
    <a class="btn" href="#">READ MORE</a>
  </article>
</section>

<footer>
  <svg class="abs footer-bg" viewBox="0 0 1200 394" aria-hidden="true">
    <path d="M0 58C150 100 330 105 560 70C800 30 1020 0 1200 30V394H0Z" fill="var(--lavender)"/>
    <path d="M0 40C150 85 330 92 560 58C800 20 1020 -8 1200 18V30C1020 0 800 30 560 70C330 105 150 100 0 58Z" fill="var(--wave)"/>
  </svg>
  <div class="brand" style="left:140px;top:3965px">
    <div class="mark" style="width:60px;height:60px"></div>
    <span style="font-size:20px">tamford</span>
  </div>
  <div class="foot-col" style="left:306px"><h4>CORPORATE</h4><ul><li>Overview</li><li>Team</li><li>Join us</li></ul></div>
  <div class="foot-col" style="left:489px"><h4>BSNS DEV</h4><ul><li>Business Development</li><li>Sales</li></ul></div>
  <div class="foot-col" style="left:717px"><h4>SERVICES</h4><ul><li>Project Management</li><li>Support</li><li>Custom Design</li></ul></div>
  <div class="foot-col" style="left:957px"><h4>CONTACT</h4><ul><li>Tamford SA de CV</li><li>Av Fundidores 12 bis</li><li>Queretaro, Mexico</li></ul></div>
  <div class="abs foot-rule"></div>
  <p class="abs copyright">Copyright © 2020 All Rights Reserved</p>
</footer>

</body>
</html>
```